Sunny Trails and joy Business card

I have a logo, but will like a business card design. Is for a travel agency in Mexico. We focus in family experiences.

I will liek some thing different and unique, from the traditional business card, something to get remmeber for.

Business card information:

Leandro R. Quiroga
leandro@sunnytrailsjoy.example

Alameda 742, 3 piso
Col. Tepalcatl
Mexico, D.F. 04910

office: (55) 4821-7390
mobile: (55) 7034-1258

www.sunnytrailsjoy.example
@sunnytjoy
blog: sunnytrailsandjoy.blog.example
facebook: SunnyTrailsAndJoy

```html
<!DOCTYPE html>
<html lang="es">
<head>
<meta charset="utf-8">
<title>Sunny Trails and joy — Tarjeta de presentación</title>
<link rel="stylesheet" href="https://fonts.googleapis.com/css2?family=Questrial&display=swap">
<style>
  :root {
    --backdrop: #e4e6e8;
    --sky-pale: #f1fafe;
    --sky-light: #bfe5f8;
    --sky: #6cc0ee;
    --sky-deep: #3f9de0;
    --band-blue: #2a78cc;
    --band-navy: #0f3c84;
    --ink-blue: #1f4f92;
    --ink-soft: #3a6aa6;
    --white: #ffffff;
    --accent-blue: #3b6fd0;
    --art-top: #a9d6f5;
    --art-bottom: #5a8fdb;
  }
  * { box-sizing: border-box; margin: 0; padding: 0; }
  html, body {
    width: 1200px; height: 731px; overflow: hidden;
    background: var(--backdrop);
    font-family: "Questrial", "Century Gothic", sans-serif;
  }
  .card {
    position: absolute; left: 410px; top: 35px;
    width: 380px; height: 660px; overflow: hidden;
    background: linear-gradient(180deg, var(--sky-pale) 0%, var(--sky-light) 28%, var(--sky) 52%, var(--sky-deep) 64%);
    box-shadow: 0 10px 26px rgba(0,0,0,.22);
  }
  .card-back-panel {
    position: absolute; left: 36px; top: 18px;
    width: 308px; height: 205px;
    transform: rotate(180deg);
    color: var(--ink-blue);
  }
  .holder-name { font-size: 21px; font-weight: 400; letter-spacing: .3px; }
  .holder-role { font-size: 12px; color: var(--ink-soft); margin-top: 2px; }
  .holder-email { font-size: 11px; margin-top: 12px; }
  .contact-lines { font-size: 11px; line-height: 1.45; margin-top: 8px; }
  .panel-brand {
    position: absolute; right: 0; bottom: 0;
    display: flex; align-items: center; gap: 5px;
    font-size: 11px; color: var(--ink-blue);
  }
  .panel-brand .dot { width: 9px; height: 9px; border-radius: 50%; background: var(--accent-blue); }
  .illustration-area {
    position: absolute; left: 70px; top: 240px;
    width: 240px; height: 130px;
    border-radius: 10px;
    background: linear-gradient(180deg, var(--art-top), var(--art-bottom));
  }
  .brand-name {
    position: absolute; left: 0; right: 0; top: 382px;
    text-align: center; font-size: 34px; line-height: 1;
    color: var(--ink-blue);
  }
  .band { position: absolute; left: 0; top: 420px; width: 380px; height: 240px; }
  .social {
    position: absolute; left: 34px; top: 478px;
    list-style: none; color: var(--white); font-size: 15px;
  }
  .social li { display: flex; align-items: center; gap: 9px; height: 25px; }
  .social .icon { width: 13px; height: 13px; border-radius: 50%; background: var(--sky-light); flex: none; }
  .website {
    position: absolute; left: 34px; top: 594px;
    color: var(--white); font-size: 21px; letter-spacing: .3px;
  }
</style>
</head>
<body>
  <article class="card">
    <section class="card-back-panel">
      <h1 class="holder-name">Leandro R. Quiroga</h1>
      <p class="holder-role">Asesor de viajes</p>
      <p class="holder-email">leandro@sunnytrailsjoy.example</p>
      <p class="contact-lines">
        office: (55) 4821-7390<br>
        mobile: (55) 7034-1258<br>
        Alameda 742, 3 piso, Col. Tepalcatl<br>
        Mexico, D.F. 04910
      </p>
      <div class="panel-brand"><span class="dot"></span>Sunny Trails and joy</div>
    </section>

    <div class="illustration-area" role="img" aria-label="Space for the brand illustration: a cheerful airplane carrying two waving children through the sky"></div>

    <p class="brand-name">Sunny Trails and joy</p>

    <svg class="band" viewBox="0 0 380 240" preserveAspectRatio="none" aria-hidden="true">
      <defs>
        <linearGradient id="bandTone" x1="0" y1="0" x2="0" y2="1">
          <stop offset="0" stop-color="#2a78cc"/>
          <stop offset="1" stop-color="#0f3c84"/>
        </linearGradient>
      </defs>
      <path d="M0 0 H380 V12 C250 40 120 38 0 26 Z" fill="#ffffff"/>
      <path d="M0 26 C120 38 250 40 380 12 V240 H0 Z" fill="url(#bandTone)"/>
    </svg>

    <ul class="social">
      <li><span class="icon"></span>@sunnytjoy</li>
      <li><span class="icon"></span>SunnyTrailsAndJoy</li>
      <li><span class="icon"></span>sunnytrailsandjoy.blog.example</li>
    </ul>
    <p class="website">www.sunnytrailsjoy.example</p>
  </article>
</body>
</html>
```